Funding your Foodie Dreams!

I need a website design for a crowdfunding site that is 100% food/beverage oriented. Artswarm is a crowdsourcing site and my site will be a crowdfunding site. It needs to be very clean, modern, BUT easy to use with a clear path to all critical elements.

This is the current site, that I need to fit into, http://www.grubnestor.com.hosted.backerhostnode.com

This site, http://tinreed.co, is PERFECT in the fact that it does not look bland or corporate in anyway and it is beautiful and effective. My site is comparable to their "Fund" section. The photo's and ease of the site is what I would love to emulate, but my site needs to be more vibrant, fun, a happy place, which can be done with colors and textures of the site. Think of food, family, local restaurants, how you feel when you are there. I would love to have that feel just from a website.

*** These sites are some sites for competitor companies and how this site needs to operate.
pledgebloom.com
dishsprout.com
coinvyrl.com
ventoraplo.com

Here are a couple sites, that I like the look of:
us.zib.com
helvaport.com
303ladlenotes.com

I would like to function like a Pledgebloom but would love it to NOT look like all the rest.
Updates

I wanted to share this site, I found today.  Love the ease of the site and the look at feel but would want mine to me more fun, food, not as ... serious... but just as professional.

http://tinreed.co

Project Deadline Extended
Reason: Hello I am extending the deadline as I have yet to receive any viable designs but received some today that with some work might be the ones so please send any designs through and please send changes through quickly. I AM expecting to award this project but with the limited # of designs, might cancel it and re-issue for a far less $ amount but make it guaranteed. Thank you very much for the few designs that have been submitted to date. C

Target Market(s)

Technically savy individuals that have an entrepreneurial spirit. Individuals that will be reaching out to friends and family to use this site who will NOT be as technologically advanced and needs the site to be very clear and easy to use but not childish.

Industry/Entity Type

Crowdfunding

Font styles to use
Sans Serif

Colors
f04950
9bcb3c
ffffff
f37123
6b449b
0555a3

Requirements
Must have
• This website will be done using a white-lable platform and so I need someone that understands the limitations of that type of a platform and can work within those boundaries.

Pages Required:
Start a Campaign
Browse Campaigns
What is grubnestor?
Help
Contact

Header & Footer

Links to Social Media
Chatterly
Peeplet
Snapvane
Tackboard
Blogsy
Nice to have
• If you can provide any coding or direction for the coding of the design in HTML, Javascript and/or CSS, these designs will have preference.

Looking for a site that will grow from only crowdfunding to include a shopping component as well as section for campaign creators to be able to get help from service providers with their campaigns maybe a blog and a forum.
Should not have
• Do NOT provide canned websites that do not meet the Must Have's. I have to use the platform format as mentioned above as I am not have a 100% custom site developed. If these sites are provided they will be eliminated immediately.

Should not resemble a corporate site in anyway.

```html
<!DOCTYPE html>
<html lang="en">
<head>
<meta charset="utf-8">
<title>grubnestor – Crowdfunding for food</title>
<link rel="stylesheet" href="https://fonts.googleapis.com/css2?family=Yanone+Kaffeesatz:wght@300;400;500&family=Arimo:wght@400&display=swap">
<style>
:root{
  --red:#d4202f;
  --red-deep:#c81b2a;
  --brown:#4a2a1c;
  --nav:#4d3a2c;
  --sky:#8ed8f8;
  --green:#6cc20a;
  --blue:#0a52a0;
  --panel:#d6dbcd;
  --ink:#1f1f1f;
  --footer:#25282c;
  --header-bg:#eceeef;
  --white:#ffffff;
}
*{margin:0;padding:0;box-sizing:border-box}
html,body{width:1200px;height:889px;overflow:hidden;background:var(--white)}
body{position:relative;font-family:"Arimo",Arial,sans-serif;color:var(--ink)}
.cond{font-family:"Yanone Kaffeesatz","Arial Narrow",sans-serif}

.site-header{position:absolute;left:0;top:0;width:1200px;height:145px;background:var(--header-bg)}
.brand{position:absolute;left:179px;top:60px;display:flex;align-items:center;gap:10px;text-decoration:none}
.brand-mark{width:46px;height:46px;background:var(--red)}
.brand-name{font-family:"Yanone Kaffeesatz",sans-serif;font-weight:400;font-size:50px;line-height:1;color:var(--brown)}
.utility-nav{position:absolute;right:211px;top:22px;display:flex;gap:10px}
.utility-nav a{font-family:"Yanone Kaffeesatz",sans-serif;font-size:19px;color:var(--red);text-decoration:none}
.main-nav{position:absolute;left:602px;top:78px;display:flex;gap:19px}
.main-nav a{font-family:"Yanone Kaffeesatz",sans-serif;font-size:21px;color:var(--nav);text-decoration:none}

.hero{position:absolute;left:0;top:145px;width:1200px;height:364px;background:var(--sky)}
.hero-photo{position:absolute;left:192px;top:0;width:469px;height:364px;background:linear-gradient(120deg,#6d6456 0%,#b8ada0 40%,#ece9e4 62%,#5a4a40 100%)}
.hero-panel{position:absolute;left:661px;top:0;width:347px;height:364px;background:var(--red-deep);text-align:center;color:var(--white)}
.hero-kicker{position:absolute;left:0;right:0;top:68px;font-size:32px;font-weight:400;line-height:1}
.hero-title{position:absolute;left:0;right:0;top:112px;font-size:56px;font-weight:500;line-height:55px}
.btn-learn{position:absolute;left:84px;top:248px;width:181px;height:62px;border:3px solid var(--white);border-radius:5px;background:var(--green);color:var(--white);font-size:30px;line-height:56px;text-decoration:none}

.feature{position:absolute;top:537px;width:300px}
.feature-campaign{left:171px}
.feature-about{left:466px}
.feature-photo{width:178px;height:118px;background:linear-gradient(135deg,#2b3a55 0%,#7d8d9c 45%,#d9dccf 65%,#5c6b3a 100%)}
.feature-icon{margin-left:64px;width:70px;height:70px;margin-top:43px;margin-bottom:5px;background:var(--red);border-radius:8px}
.feature h2{margin:14px 0 0 2px;font-size:29px;font-weight:400;line-height:1;color:var(--ink)}
.feature p{margin:6px 0 0 2px;font-size:11.5px;line-height:18.6px;color:var(--ink)}

.login-box{position:absolute;left:752px;top:543px;width:238px;height:270px;background:var(--panel)}
.login-box h2{position:absolute;left:22px;top:13px;font-size:29px;font-weight:400;color:var(--ink)}
.login-box label{position:absolute;left:21px;font-size:11.5px;color:var(--ink)}
.login-box input{position:absolute;left:20px;width:159px;height:35px;border:1px solid #b9bcb3;background:var(--white)}
.btn-login{position:absolute;left:23px;top:207px;width:87px;height:38px;border-radius:19px;background:var(--blue);color:var(--white);font-size:22px;line-height:38px;text-align:center;text-decoration:none}
.link-register{position:absolute;left:124px;top:218px;font-size:17px;color:var(--red);text-decoration:none}

.site-footer{position:absolute;left:0;top:849px;width:1200px;height:40px;background:var(--footer);border-top:2px solid #141618}
.copyright{position:absolute;left:172px;top:11px;font-size:10px;color:#e6e6e6}
.copyright a{color:#e6e6e6;text-decoration:none}
.social{position:absolute;left:790px;top:7px;width:124px;height:26px;background:#1a1c1f;display:flex;gap:8px;align-items:center;padding-left:8px}
.social a{width:17px;height:17px;background:#e8e8e8;border-radius:2px}
</style>
</head>
<body>
<header class="site-header">
  <a class="brand" href="#"><span class="brand-mark"></span><span class="brand-name">grubnestor</span></a>
  <nav class="utility-nav"><a href="#">Login</a><a href="#">Help</a><a href="#">Contact</a></nav>
  <nav class="main-nav"><a href="#">Start a Campaign</a><a href="#">Browse Campaigns</a><a href="#">What is grubnestor?</a></nav>
</header>

<section class="hero">
  <div class="hero-photo" role="img" aria-label="Photo of a smiling waitress serving a diner at a restaurant table"></div>
  <div class="hero-panel cond">
    <p class="hero-kicker">WELCOME TO YOUR NEW</p>
    <h1 class="hero-title">CROWDFUNDING<br>PLATFORM</h1>
    <a class="btn-learn" href="#">LEARN MORE</a>
  </div>
</section>

<article class="feature feature-campaign">
  <div class="feature-photo" role="img" aria-label="Photo of a hand holding a megaphone"></div>
  <h2 class="cond">Start a Campaign</h2>
  <p>Lorem ipsum dolor sit amet, consectetur adip-<br>isicing elit, sed do eiusmod tempor incididunt ut<br>labore et dolore magna aliqua. Ut enim ad minim</p>
</article>

<article class="feature feature-about">
  <div class="feature-icon"></div>
  <h2 class="cond">What is grubnestor</h2>
  <p>Tubewell Works is the largest provider of poly-<br>ethylene pipe (poly pipe) - HDPE pressure pipe<br>and fittings in North America</p>
</article>

<form class="login-box">
  <h2 class="cond">Login</h2>
  <label style="top:72px" for="user">Username</label>
  <input id="user" type="text" style="top:81px">
  <label style="top:143px" for="pass">Password</label>
  <input id="pass" type="password" style="top:155px">
  <a class="btn-login cond" href="#">LOGIN</a>
  <a class="link-register cond" href="#">REGISTER</a>
</form>

<footer class="site-footer">
  <p class="copyright">Copyright 2013 grubnestor - <a href="#">Terms &amp; Conditions</a> | <a href="#">Privacy Policy</a></p>
  <nav class="social">
    <a href="#" aria-label="Peeplet"></a>
    <a href="#" aria-label="Chatterly"></a>
    <a href="#" aria-label="Tackboard"></a>
    <a href="#" aria-label="Linkwell"></a>
    <a href="#" aria-label="Blogsy"></a>
  </nav>
</footer>
</body>
</html>
```